Business card for massage therapy company called Brook Fern Wellness

Need business card for massage therapy company called Brook Fern Wellness. Would like my logo on the front and the back of the card I have 3 options of logos and you can play with what looks better.

Would like this information displayed on the back of the card:

Marcus Ellery
Licensed Massage Therapist
321-555-0147
brookfern-example.com
brookfern_rest_

```html
<!DOCTYPE html>
<html lang="en">
<head>
<meta charset="utf-8">
<title>Brook Fern Wellness – Business Card</title>
<link href="https://fonts.googleapis.com/css2?family=Jost:wght@300;400&family=EB+Garamond:wght@400&display=swap" rel="stylesheet">
<style>
  :root {
    --backdrop: #2b2b2b;
    --sage: #6c7458;
    --sage-edge: #5d6449;
    --paper: #f5f4ef;
    --ink: #5a5c4e;
    --clay: #a47f70;
    --rule: #c2a89c;
    --cream: #fbfaf5;
    --leaf-a: rgba(190, 200, 175, 0.55);
    --leaf-b: rgba(190, 200, 175, 0);
  }
  * { margin: 0; padding: 0; box-sizing: border-box; }
  html, body { width: 1200px; height: 900px; overflow: hidden; background: var(--backdrop); }
  .canvas { position: relative; width: 1200px; height: 900px; }

  .card { position: absolute; left: 278px; width: 648px; height: 347px; border-radius: 22px; overflow: hidden; }
  .card-front { top: 112px; background: var(--sage); box-shadow: 0 4px 0 var(--sage-edge); }
  .card-back { top: 486px; background: var(--paper); }

  .brand-ring { position: absolute; border-radius: 50%; }
  .card-front .brand-ring { left: 530px; top: 48px; width: 140px; height: 140px; border: 1.5px solid var(--cream); left: 255px; }
  .brand-name {
    position: absolute; left: 0; right: 0; text-align: center;
    font-family: 'Jost', sans-serif; font-weight: 300; text-transform: uppercase;
  }
  .card-front .brand-name { top: 222px; color: var(--cream); font-size: 40px; letter-spacing: 5px; line-height: 1.3; }

  .back-brand { position: absolute; left: 22px; top: 40px; width: 160px; height: 160px; }
  .card-back .brand-ring { left: 50px; top: 14px; width: 92px; height: 92px; border: 1.3px solid var(--ink); left: 34px; }
  .card-back .brand-name { top: 114px; color: var(--ink); font-size: 18px; letter-spacing: 2px; line-height: 1.35; }

  .divider { position: absolute; left: 191px; top: 54px; width: 1px; height: 230px; background: var(--rule); }

  .person { position: absolute; left: 224px; top: 52px; font-family: 'EB Garamond', serif; }
  .person-name { color: var(--ink); font-size: 33px; line-height: 1; }
  .person-role { color: var(--clay); font-size: 20px; margin-top: 16px; letter-spacing: 0.3px; }
  .person-rule { width: 300px; height: 1px; background: var(--rule); margin-top: 18px; }

  .contacts { list-style: none; margin-top: 22px; }
  .contacts li { display: flex; align-items: center; height: 40px; color: var(--ink); font-size: 20px; }
  .contacts svg, .contacts .social-dot { width: 20px; height: 20px; margin-right: 13px; flex: none; }
  .social-dot { border: 1.6px solid var(--ink); border-radius: 50%; }

  .foliage {
    position: absolute; right: 0; bottom: 0; width: 270px; height: 220px;
    background: radial-gradient(ellipse at 80% 70%, var(--leaf-a), var(--leaf-b) 70%);
  }
</style>
</head>
<body>
<div class="canvas">
  <section class="card card-front">
    <div class="brand-ring"></div>
    <div class="brand-name">Brook Fern<br>Wellness</div>
  </section>

  <section class="card card-back">
    <div class="foliage" role="img" aria-label="Soft watercolour sprig of pale sage leaves"></div>
    <div class="back-brand">
      <div class="brand-ring"></div>
      <div class="brand-name">Brook Fern<br>Wellness</div>
    </div>
    <div class="divider"></div>
    <div class="person">
      <div class="person-name">Marcus Ellery</div>
      <div class="person-role">Licensed Massage Therapist</div>
      <div class="person-rule"></div>
      <ul class="contacts">
        <li>
          <svg viewBox="0 0 24 24" aria-hidden="true"><path fill="#5a5c4e" d="M6.6 10.8a15.1 15.1 0 0 0 6.6 6.6l2.2-2.2a1 1 0 0 1 1-.25 11.4 11.4 0 0 0 3.6.57 1 1 0 0 1 1 1V20a1 1 0 0 1-1 1A17 17 0 0 1 3 4a1 1 0 0 1 1-1h3.5a1 1 0 0 1 1 1c0 1.25.2 2.45.57 3.57a1 1 0 0 1-.25 1z"/></svg>
          321-555-0147
        </li>
        <li>
          <svg viewBox="0 0 24 24" aria-hidden="true" fill="none" stroke="#5a5c4e" stroke-width="1.5"><circle cx="12" cy="12" r="9.5"/><ellipse cx="12" cy="12" rx="4.2" ry="9.5"/><path d="M2.5 12h19M4 7h16M4 17h16"/></svg>
          brookfern-example.com
        </li>
        <li>
          <span class="social-dot" aria-hidden="true"></span>
          brookfern_rest_
        </li>
      </ul>
    </div>
  </section>
</div>
</body>
</html>
```